VBN Line Card

We are looking for a line card to leave with potential customers.
Logo on top

VBN is a Colorado-based business specializing in demolition, materials management, hazardous materials management, and trucking & hauling. What differentiates VBN is our breadth of experience in upcycling much of reusable debris from the demolition process for reuse on existing projects or recycling the material for later use on other projects.

We offer an end-to-end client experience that includes seamless communication, budgeting, staffing, on-site organization, and solid, quality work every time.

Trucking and Hauling Equipment:
30 yd End Dump
Steel Side Scrap Trailer
90 yr End Dump
Flatbeds
70 Ton Lowboy Trailer 2-3-2 combo

Gordon Ellery
President
720-463-9170
gellery@vbnmetalworks.com

I'd like it to be easy to read, but look modern

Target Market(s)

General Contractors

Industry/Entity Type

Construction

Colors
EB3D1F
EC4F4E
F09395
F8D3D4
FCEDEE

Requirements
Must have
• Our colors and red and gun metal gray

```html
<!DOCTYPE html>
<html lang="en">
<head>
<meta charset="utf-8">
<title>VBN Line Card</title>
<link href="https://fonts.googleapis.com/css2?family=Exo+2:ital,wght@1,900&family=Michroma&family=Poppins:wght@400;500;600;700;800&display=swap" rel="stylesheet">
<style>
  :root {
    --brand-red: #8e1c1e;
    --brand-red-deep: #7a1517;
    --accent-red: #eb3d1f;
    --gunmetal: #1f1f21;
    --ink: #222226;
    --stage: #8a8a8c;
    --paper: #ffffff;
    --photo-light: #eceef0;
    --photo-steel: #6d6f75;
    --divider: #c9c9cc;
  }
  * { box-sizing: border-box; margin: 0; padding: 0; }
  html, body { width: 1200px; height: 2330px; overflow: hidden; }
  body { background: var(--stage); font-family: "Poppins", sans-serif; color: var(--ink); position: relative; }

  .line-card {
    position: absolute; left: 50px; top: 453px;
    width: 1000px; height: 1295px;
    transform: scale(1.1); transform-origin: 0 0;
    background: var(--paper); overflow: hidden;
    box-shadow: 0 20px 40px rgba(0,0,0,.35);
  }
  .side-panel { position: absolute; left: 670px; top: 0; width: 330px; height: 100%; background: var(--brand-red); }
  .abs { position: absolute; }

  .wordmark { left: 45px; top: 38px; font-family: "Poppins", sans-serif; font-weight: 800; font-size: 84px; line-height: 1; color: var(--brand-red); letter-spacing: 6px; }
  .kicker { left: 50px; top: 168px; font-family: "Michroma", sans-serif; font-size: 25px; letter-spacing: 8px; color: var(--ink); }
  .headline { left: 44px; top: 198px; font-family: "Exo 2", sans-serif; font-style: italic; font-weight: 900; font-size: 62px; line-height: 56px; color: var(--brand-red); letter-spacing: 1px; }
  .headline-sub { left: 46px; top: 318px; font-family: "Michroma", sans-serif; font-size: 30px; font-weight: 400; color: var(--ink); -webkit-text-stroke: 1px var(--ink); }

  .hero-photo { left: 560px; top: 58px; width: 440px; height: 410px; background: linear-gradient(160deg, #b9b3a6 0%, #4f5159 55%, #2b2c31 100%); clip-path: polygon(30% 30%, 62% 0, 100% 0, 100% 100%, 8% 100%, 0 60%); }

  .specialty-bar { left: 0; top: 386px; width: 355px; height: 46px; background: var(--gunmetal); border-radius: 0 10px 10px 0; color: #fff; font-size: 29px; line-height: 46px; padding-left: 45px; box-shadow: 0 4px 6px rgba(0,0,0,.25); }
  .specialty-bar strong { font-weight: 700; }

  .specialties { left: 30px; top: 455px; width: 560px; display: flex; }
  .specialty { flex: 1; text-align: center; font-weight: 600; font-size: 16px; line-height: 19px; color: var(--ink); border-right: 2px solid var(--divider); height: 130px; }
  .specialty:last-child { border-right: none; }
  .specialty svg { display: block; margin: 0 auto 14px; }

  .intro { left: 43px; top: 612px; width: 545px; font-size: 16.5px; line-height: 19.5px; color: var(--ink); }

  .equip-title { left: 45px; top: 705px; font-size: 28px; font-weight: 700; color: var(--brand-red); line-height: 30px; }
  .equip-sub { left: 45px; top: 738px; font-size: 26px; font-weight: 400; color: var(--ink); line-height: 30px; }
  .equip-rule { left: 215px; top: 762px; width: 360px; height: 2px; background: var(--ink); }

  .equip-tile { width: 258px; height: 146px; border: 3px solid var(--brand-red); border-radius: 6px; overflow: hidden; background: var(--brand-red); }
  .equip-tile .photo { height: 108px; background: linear-gradient(180deg, #ffffff 0%, var(--photo-light) 100%); border-radius: 3px 3px 0 0; }
  .equip-tile .label { color: #fff; text-align: center; font-size: 14px; font-weight: 600; line-height: 32px; white-space: nowrap; }

  .fleet-photo { left: 325px; top: 1125px; width: 330px; height: 115px; background: linear-gradient(90deg, #b21f22 0%, #d93a30 55%, #8e1c1e 100%); border-radius: 30px 8px 8px 30px; }

  .offer { left: 690px; top: 520px; width: 260px; color: #fff; font-size: 21px; line-height: 21px; }
  .offer strong { display: block; font-weight: 700; }
  .offer-rule { left: 690px; top: 618px; width: 265px; height: 2px; background: rgba(255,255,255,.6); }

  .benefits { left: 643px; top: 640px; width: 320px; list-style: none; }
  .benefit { display: flex; align-items: center; height: 75px; border-bottom: 1px solid rgba(0,0,0,.22); }
  .benefit svg { flex: none; margin-right: 16px; }
  .benefit span { color: #fff; font-size: 18.5px; font-weight: 500; line-height: 21px; }

  .portrait { left: 575px; top: 1025px; width: 200px; height: 270px; background: linear-gradient(180deg, #c9a893 0%, #9a8273 60%, #6b5a52 100%); border-radius: 100px 100px 0 0; }

  .contact-pill { left: 710px; top: 1080px; width: 245px; height: 66px; background: var(--gunmetal); border-radius: 14px 0 14px 14px; color: #fff; padding: 8px 0 0 35px; }
  .contact-name { font-size: 25px; line-height: 28px; text-transform: uppercase; white-space: nowrap; }
  .contact-name strong { font-weight: 700; }
  .contact-role { font-size: 17px; line-height: 20px; }
  .contact-line { left: 760px; color: #fff; font-size: 14px; line-height: 18px; display: flex; align-items: center; gap: 6px; white-space: nowrap; }
  .web { left: 760px; top: 1226px; width: 225px; color: #fff; font-size: 16px; letter-spacing: 1.2px; white-space: nowrap; }
  .web b { font-weight: 700; }
</style>
</head>
<body>
<main class="line-card">
  <div class="side-panel"></div>

  <div class="abs hero-photo" role="img" aria-label="Photo of a tipper dump truck with raised bed"></div>

  <div class="abs wordmark">VBN</div>
  <p class="abs kicker">A COLORADO-BASED</p>
  <h1 class="abs headline">TRUCKING<br>&amp; HAULING</h1>
  <p class="abs headline-sub">EQUIPMENT BUSINESS</p>

  <div class="abs specialty-bar">WE <strong>SPECIALIZING IN</strong></div>

  <div class="abs specialties">
    <div class="specialty">
      <svg width="60" height="60" viewBox="0 0 60 60"><circle cx="30" cy="30" r="29" fill="none" stroke="#8e1c1e" stroke-dasharray="3 2"/><circle cx="30" cy="30" r="25" fill="#1f1f21"/><path d="M20 40h20v-6h-8l-6-12-4 2 5 10h-7z" fill="#fff"/></svg>
      Demolition
    </div>
    <div class="specialty">
      <svg width="60" height="60" viewBox="0 0 60 60"><circle cx="30" cy="30" r="29" fill="none" stroke="#8e1c1e" stroke-dasharray="3 2"/><circle cx="30" cy="30" r="25" fill="#1f1f21"/><rect x="23" y="24" width="14" height="13" fill="#fff"/><path d="M18 30a12 12 0 0 1 20-9" stroke="#fff" stroke-width="2" fill="none"/></svg>
      Materials<br>management
    </div>
    <div class="specialty">
      <svg width="60" height="60" viewBox="0 0 60 60"><circle cx="30" cy="30" r="29" fill="none" stroke="#8e1c1e" stroke-dasharray="3 2"/><circle cx="30" cy="30" r="25" fill="#1f1f21"/><circle cx="25" cy="34" r="6" fill="none" stroke="#fff" stroke-width="3"/><rect x="30" y="18" width="10" height="10" fill="#fff"/></svg>
      Hazardous<br>materials<br>management
    </div>
    <div class="specialty">
      <svg width="60" height="60" viewBox="0 0 60 60"><circle cx="30" cy="30" r="29" fill="none" stroke="#8e1c1e" stroke-dasharray="3 2"/><circle cx="30" cy="30" r="25" fill="#1f1f21"/><rect x="21" y="19" width="18" height="20" rx="3" fill="#fff"/><rect x="24" y="22" width="12" height="6" fill="#1f1f21"/></svg>
      Trucking &amp;<br>hauling
    </div>
  </div>

  <p class="abs intro">What differentiates VBN is our breadth of experience in upcycling much of reusable debris from the demolition process for reuse on existing projects or recycling the material for later use on other projects.</p>

  <h2 class="abs equip-title">TRUCKING AND HAULING</h2>
  <p class="abs equip-sub">EQUIPMENT</p>
  <div class="abs equip-rule"></div>

  <div class="abs equip-tile" style="left:47px;top:788px"><div class="photo" role="img" aria-label="White box truck"></div><div class="label">30 yd End Dump</div></div>
  <div class="abs equip-tile" style="left:319px;top:788px"><div class="photo" role="img" aria-label="Blue steel side scrap trailer truck"></div><div class="label">Steel Side Scrap Trailer</div></div>
  <div class="abs equip-tile" style="left:47px;top:945px"><div class="photo" role="img" aria-label="Orange end dump truck"></div><div class="label">90 yr End Dump</div></div>
  <div class="abs equip-tile" style="left:319px;top:945px"><div class="photo" role="img" aria-label="Flatbed truck"></div><div class="label">Flatbeds</div></div>
  <div class="abs equip-tile" style="left:47px;top:1102px"><div class="photo" role="img" aria-label="Lowboy trailer truck"></div><div class="label">70 Ton Lowboy Trailer 2-3-2 combo</div></div>

  <div class="abs fleet-photo" role="img" aria-label="Red semi truck with end dump trailer"></div>

  <p class="abs offer">WE OFFER AN<strong>END-TO-END CLIENT EXPERIENCE THAT INCLUDE</strong></p>
  <div class="abs offer-rule"></div>

  <ul class="abs benefits">
    <li class="benefit"><svg width="60" height="60" viewBox="0 0 60 60"><circle cx="30" cy="30" r="29" fill="#fff"/><circle cx="30" cy="30" r="25" fill="#1f1f21"/><circle cx="24" cy="26" r="4" fill="#fff"/><circle cx="36" cy="26" r="4" fill="#fff"/><path d="M17 40a7 7 0 0 1 14 0zM29 40a7 7 0 0 1 14 0z" fill="#fff"/></svg><span>Seamless<br>communication</span></li>
    <li class="benefit"><svg width="60" height="60" viewBox="0 0 60 60"><circle cx="30" cy="30" r="29" fill="#fff"/><circle cx="30" cy="30" r="25" fill="#1f1f21"/><path d="M30 18a12 12 0 1 0 12 12H30z" fill="#fff"/><path d="M32 16v12h12a12 12 0 0 0-12-12z" fill="#fff"/></svg><span>Budgeting</span></li>
    <li class="benefit"><svg width="60" height="60" viewBox="0 0 60 60"><circle cx="30" cy="30" r="29" fill="#fff"/><circle cx="30" cy="30" r="25" fill="#1f1f21"/><circle cx="30" cy="24" r="5" fill="#fff"/><path d="M19 41a11 9 0 0 1 22 0z" fill="#fff"/></svg><span>Staffing</span></li>
    <li class="benefit"><svg width="60" height="60" viewBox="0 0 60 60"><circle cx="30" cy="30" r="29" fill="#fff"/><circle cx="30" cy="30" r="25" fill="#1f1f21"/><circle cx="30" cy="32" r="9" fill="none" stroke="#fff" stroke-width="3"/><path d="M26 32l3 3 5-6" stroke="#fff" stroke-width="2.5" fill="none"/><rect x="25" y="17" width="10" height="5" fill="#fff"/></svg><span>On-site<br>organization</span></li>
    <li class="benefit"><svg width="60" height="60" viewBox="0 0 60 60"><circle cx="30" cy="30" r="29" fill="#fff"/><circle cx="30" cy="30" r="25" fill="#1f1f21"/><rect x="19" y="26" width="8" height="15" fill="#fff"/><rect x="27" y="19" width="8" height="22" fill="#fff"/><rect x="35" y="28" width="7" height="13" fill="#fff"/></svg><span>Solid quality work<br>every time</span></li>
  </ul>

  <div class="abs portrait" role="img" aria-label="Portrait of the company president"></div>

  <div class="abs contact-pill">
    <p class="contact-name"><strong>Gordon</strong> Ellery</p>
    <p class="contact-role">President</p>
  </div>
  <p class="abs contact-line" style="top:1157px"><svg width="12" height="12" viewBox="0 0 12 12"><path d="M2 1l2.5 0 1 3-1.5 1a7 7 0 0 0 3 3l1-1.5 3 1V10a1 1 0 0 1-1 1A10 10 0 0 1 1 2a1 1 0 0 1 1-1z" fill="#fff"/></svg>720-463-9170</p>
  <p class="abs contact-line" style="top:1180px"><svg width="12" height="10" viewBox="0 0 12 10"><rect x="0.5" y="0.5" width="11" height="9" fill="#fff"/><path d="M.5.5l5.5 5 5.5-5" stroke="#8e1c1e" fill="none"/></svg>gellery@vbnmetalworks.com</p>
  <p class="abs web">www.<b>vbnmetalworks</b>.com</p>
</main>
</body>
</html>
```